Business Card Design

I am specialising in Designs, Drafting and Council approvals. From the idea to the full set of plans and other documents. Residential houses only.
I am located in Northern Beaches, Sydney where the sky is always blue :)
Tallwood Drafting should be associated with light, modern house designs & with 3D drafting. I am positive person, that would like help every client through the demanding time of council paperwork.

The business card should be light blue, with white 3D sketch and white or black writing. Simple, modern and "happy"

Please don't hesitate to suggest something if you think so.

Thanks
Mirela

Industry/Entity Type

House

Contact Information for Business Card

FRONT:

Tallwood Drafting
Servicing Northern Beaches

Mirela Ostrowe
tallwooddrafting@mailhaven.com.au
0427 586 293
www.tallwooddrafting.com.au

BACK:

Design consultation
Plans Drafting
3D Visualisation
Council Approvals

```html
<!DOCTYPE html>
<html lang="en">
<head>
<meta charset="utf-8">
<title>Tallwood Drafting — Business Card</title>
<link rel="stylesheet" href="https://fonts.googleapis.com/css2?family=Roboto+Slab:wght@800&family=Roboto+Condensed:wght@400;700&display=swap">
<style>
  :root {
    --canvas-bg: #e9ecef;
    --sky-light: #eef5f8;
    --sky-mid: #a9d3de;
    --sky-aqua: #7cc3d2;
    --sky-deep: #3f7d9c;
    --navy: #1f4f70;
    --ink-white: #ffffff;
    --title-shadow: rgba(20, 55, 80, 0.55);
    --rule: rgba(255, 255, 255, 0.75);
  }
  * { margin: 0; padding: 0; box-sizing: border-box; }
  html, body {
    width: 1200px; height: 1000px; overflow: hidden;
    background: var(--canvas-bg);
  }
  .canvas {
    width: 1200px; height: 1000px;
    display: flex; flex-direction: column; align-items: center; justify-content: center;
    gap: 48px;
  }
  .card {
    position: relative;
    width: 720px; height: 436px;
    border-radius: 26px;
    overflow: hidden;
    box-shadow: 0 8px 24px rgba(30, 60, 90, 0.18);
    color: var(--ink-white);
  }
  .brand-title {
    position: relative;
    font-family: "Roboto Slab", Georgia, serif;
    font-weight: 800;
    font-size: 40px;
    line-height: 1.1;
    letter-spacing: 0.08em;
    text-transform: uppercase;
    color: var(--ink-white);
    text-shadow: 2px 2px 0 var(--title-shadow);
    white-space: nowrap;
  }
  .condensed {
    position: relative;
    font-family: "Roboto Condensed", "Arial Narrow", sans-serif;
    font-weight: 700;
    letter-spacing: 0.04em;
    text-shadow: 1px 1px 1px rgba(20, 55, 80, 0.5);
    white-space: nowrap;
  }

  /* Services side */
  .card--services {
    background: linear-gradient(200deg, var(--sky-light) 0%, #d8ecf2 30%, var(--sky-mid) 58%, var(--sky-deep) 100%);
  }
  .services__plan {
    position: absolute; left: 0; top: 90px; width: 420px; height: 346px;
    background: radial-gradient(ellipse at 40% 60%, rgba(255,255,255,0.28), rgba(255,255,255,0) 70%);
  }
  .services__content {
    position: absolute; left: 56px; right: 40px; top: 150px;
  }
  .services__list {
    margin-top: 14px; font-size: 22px; line-height: 1.4;
  }
  .services__list--second { margin-top: 6px; margin-left: 150px; }

  /* Contact side */
  .card--contact {
    background: linear-gradient(20deg, var(--navy) 0%, var(--sky-deep) 32%, var(--sky-aqua) 65%, #cfe7ee 100%);
  }
  .contact__house {
    position: absolute; right: 30px; top: 24px; width: 320px; height: 290px;
    background: linear-gradient(160deg, rgba(255,255,255,0.5), rgba(255,255,255,0.1) 75%);
    border-radius: 6px;
  }
  .contact__heading { position: absolute; left: 40px; top: 60px; }
  .contact__tagline { margin-top: 12px; font-size: 20px; }
  .contact__rule {
    position: absolute; left: 30px; right: 30px; bottom: 80px;
    height: 2px; background: var(--rule);
  }
  .contact__details {
    position: absolute; left: 40px; right: 40px; bottom: 40px;
    display: flex; justify-content: space-between; gap: 24px;
    font-size: 16px; font-weight: 400;
  }
  .contact__details span { white-space: nowrap; }
</style>
</head>
<body>
<main class="canvas">

  <section class="card card--services" aria-label="Card back with services">
    <div class="services__plan" role="img" aria-label="Faint white architectural floor plan drawing"></div>
    <div class="services__content">
      <h1 class="brand-title">Tallwood Drafting</h1>
      <p class="services__list condensed">Design consultation &bull; Plans &bull; Drafting &bull; 3D Visualisation</p>
      <p class="services__list services__list--second condensed">Council &bull; Approvals</p>
    </div>
  </section>

  <section class="card card--contact" aria-label="Card front with contact details">
    <div class="contact__house" role="img" aria-label="White 3D sketch of a modern two-storey house"></div>
    <div class="contact__heading">
      <h2 class="brand-title">Tallwood Drafting</h2>
      <p class="contact__tagline condensed">Servicing Northern Beaches Mirela Ostrowe</p>
    </div>
    <div class="contact__rule"></div>
    <p class="contact__details condensed">
      <span class="contact__email">tallwooddrafting@mailhaven.com.au</span>
      <span class="contact__phone">0427 586 293</span>
      <span class="contact__web">www.tallwooddrafting.com.au</span>
    </p>
  </section>

</main>
</body>
</html>
```